Managed Service Provider VOIP Flyer

Looking for a one page US letter size single or double sided brochure to offer cloud hosted VoIP Phone system and unified communications. We have partnered with a VoIP Phone system company and want to sell their services but we don't want their name to be shown on the brochure because customers might call them directly. The company name is Corlune (www.corlune-example.com) and our company name is Gear With Rowena, LLC and our voice product is called Plainly Talk. I have also uploaded my company's logo that you should show on the brochure and use that coloring. For more details about the product, you can visit their website mentioned above. Also I am looking for something very similar to this project and many of the technical details are the same https://flyer.examplecontests.net/contest/5817264

I have also uploaded a PDF with my different package levels and some of the included features. Depending on the design we may or may not want the package levels on this flyer.

Target Market(s)

Small and medium Businesses

Industry/Entity Type

Voip

Requirements
Must have
• Feature and benefits information of Handled TALK. Use my logo and coloring from my logo. Include our website, email, phone and possibly facebook if it makes sense/looks good.

www.gearwithrowena.net
415.639.0.517
sales@gearwithrowena.net
www.facebook.com/gearwithrowena
Nice to have
• Would like to show how the service is simple and reliable and available for any business size

```html
<!DOCTYPE html>
<html lang="en">
<head>
<meta charset="utf-8">
<title>Plainly Talk – Gear With Rowena</title>
<link href="https://fonts.googleapis.com/css2?family=Jost:wght@400;500&display=swap" rel="stylesheet">
<style>
:root{
  --navy:#1b3a6b;
  --navy-dark:#14284c;
  --red:#bd2a2e;
  --grey-row:#e3e5ea;
  --text-grey:#5d6470;
  --stage:#a9aaae;
  --white:#ffffff;
}
*{box-sizing:border-box;margin:0;padding:0}
html,body{width:1200px;height:889px;overflow:hidden}
body{background:var(--stage);font-family:'Jost',sans-serif;position:relative}
.page{position:absolute;top:73px;width:918px;height:1298px;background:var(--white);transform:scale(.5376);transform-origin:0 0;overflow:hidden}
.page--front{left:72px}
.page--back{left:630px}
.abs{position:absolute}
.shapes{position:absolute;left:0;top:0}
.brand{display:flex;align-items:center;gap:16px;color:var(--navy);font-weight:500;font-size:46px;line-height:1;text-transform:uppercase}
.brand__square{width:34px;height:34px;background:var(--red)}
.brand__name{display:flex;flex-direction:column}
.headline{color:var(--navy);font-weight:500;font-size:50px}
.checklist{list-style:none;color:var(--navy);font-size:22px;line-height:1.25}
.checklist li{display:flex;gap:16px;margin-bottom:14px}
.checklist svg{flex:none;margin-top:3px}
.hex-badge{color:var(--white);font-size:32px;line-height:1.03;text-align:center;font-weight:500}
.seat-title{color:var(--white);font-size:40px;font-weight:400}
.seat-list{list-style:none;color:var(--white);font-size:19px}
.seat-list li{display:flex;align-items:center;gap:18px;height:37.2px}
.pitch{color:var(--navy);font-size:24px;line-height:1.24;text-align:center;width:370px}
.pitch p+p{margin-top:14px}
.cta{color:var(--red);font-size:20.5px;line-height:1.3;text-align:center;width:340px}
.contacts{color:var(--navy);font-size:17px;text-align:center;width:380px;line-height:1.6}
.contacts .phone{color:var(--red);font-size:20px}
.contacts span{display:inline-flex;align-items:center;gap:6px}
.footer{position:absolute;left:0;bottom:0;width:918px;height:52px;background:var(--red);color:var(--white);display:flex;align-items:center}
.footer__strip{position:absolute;right:0;bottom:0;width:270px;height:6px;background:var(--navy)}
.footer .web{display:inline-flex;align-items:center;gap:8px}
.addon-title{color:var(--navy);font-size:28px;font-weight:500}
.addon h3{color:var(--red);font-size:15px;font-weight:500}
.addon p{color:var(--text-grey);font-size:13.4px;line-height:1.38}
.plan-head{position:absolute;left:45px;top:283px;width:820px;height:85px;background:linear-gradient(90deg,var(--navy-dark) 0%,var(--navy) 60%,#2c4f86 100%);color:var(--white)}
.plan-head__title{position:absolute;left:30px;top:26px;font-size:36px;font-weight:500}
.plan{position:absolute;top:16px;text-align:center;width:180px;margin-left:-90px}
.plan__name{color:var(--red);font-size:27px;line-height:1;font-weight:500}
.plan__sub{font-size:15px}
.price-bar{position:absolute;left:45px;top:368px;width:820px;height:18px;background:var(--red);color:var(--white);font-size:14px;padding-left:13px;line-height:20px}
.price{position:absolute;top:350px;width:58px;margin-left:-29px;height:34px;background:var(--navy);border:1px solid var(--white);color:var(--white);font-size:20px;text-align:center;line-height:32px}
.plan-table{position:absolute;left:45px;top:389px;width:820px;color:var(--text-grey);font-size:14.5px}
.row{display:grid;grid-template-columns:283px 182px 182px 173px;height:21.6px;align-items:center}
.row:nth-child(even){background:var(--grey-row)}
.row--tall{height:40px;line-height:1.1}
.row>span:first-child{padding-left:13px;color:#555c66}
.row>span{text-align:center;color:#333a44}
.row>span:first-child{text-align:left}
.cell{display:flex;justify-content:center;align-items:center;gap:6px;font-size:14.5px}
.cell small{font-size:11px;position:absolute;margin-left:80px}
.pbx-box{position:absolute;left:20px;top:910px;width:872px;height:330px;background:linear-gradient(135deg,var(--navy) 0%,#213f73 100%);color:var(--white)}
.pbx-pill{position:absolute;left:208px;top:892px;width:478px;height:40px;border-radius:20px;background:var(--white);border:2px solid var(--navy);color:var(--navy);font-size:24px;text-align:center;line-height:36px}
.pbx-col h4{font-size:15px;font-weight:500}
.pbx-col p{font-size:13.8px;line-height:1.36;color:#dfe5ef;margin-bottom:14px}
.back-footer{font-size:14px;gap:0}
</style>
</head>
<body>
<svg width="0" height="0" style="position:absolute">
  <defs>
    <symbol id="tick" viewBox="0 0 14 14"><circle cx="7" cy="7" r="6" fill="none" stroke="#bd2a2e" stroke-width="1.3"/><path d="M4 7.2l2 2 4-4.4" fill="none" stroke="#bd2a2e" stroke-width="1.5"/></symbol>
    <symbol id="cross" viewBox="0 0 14 14"><circle cx="7" cy="7" r="6" fill="none" stroke="#6b7280" stroke-width="1.2"/><path d="M4.6 4.6l4.8 4.8M9.4 4.6l-4.8 4.8" stroke="#6b7280" stroke-width="1.4"/></symbol>
    <symbol id="box-check" viewBox="0 0 22 22"><rect x="1.5" y="3.5" width="17" height="17" fill="none" stroke="#bd2a2e" stroke-width="2.4"/><path d="M5 11l4 4 11-13" fill="none" stroke="#bd2a2e" stroke-width="2.6"/></symbol>
    <symbol id="handset" viewBox="0 0 24 24"><path d="M6.5 2.5l3 4-2 2.2c1 2.5 3.3 4.9 5.8 5.8l2.2-2 4 3-1.8 3.2C12 18.5 5.3 11.8 3.3 4.3z" fill="#fff"/></symbol>
    <symbol id="globe" viewBox="0 0 20 20"><circle cx="10" cy="10" r="8" fill="none" stroke="currentColor" stroke-width="1.6"/><path d="M2 10h16M10 2c-3 3-3 13 0 16M10 2c3 3 3 13 0 16" fill="none" stroke="currentColor" stroke-width="1.4"/></symbol>
    <symbol id="phone-line" viewBox="0 0 20 20"><path d="M5.5 2l2.6 3.4-1.7 1.9c.9 2.1 2.8 4.1 4.9 4.9l1.9-1.7L16.6 13l-1.5 2.7C9.6 14.9 4 9.3 3 3.8z" fill="none" stroke="currentColor" stroke-width="1.5"/></symbol>
    <symbol id="mail" viewBox="0 0 20 20"><rect x="2" y="4.5" width="16" height="11" fill="none" stroke="currentColor" stroke-width="1.5"/><path d="M2 5l8 6 8-6" fill="none" stroke="currentColor" stroke-width="1.5"/></symbol>
    <linearGradient id="photo-tones" x1="0" y1="0" x2="1" y2="1"><stop offset="0" stop-color="#1a2340"/><stop offset=".5" stop-color="#3a4f78"/><stop offset="1" stop-color="#6a2330"/></linearGradient>
  </defs>
</svg>

<!-- FRONT -->
<section class="page page--front">
  <svg class="shapes" width="918" height="1298" viewBox="0 0 918 1298">
    <polygon points="368,165 600,0 918,0 918,470 640,620 368,455" fill="#1b3a6b"/>
    <polygon points="575,470 902,470 902,600 660,620 575,560" fill="#1b3a6b"/>
    <polygon points="0,545 165,492 460,660 460,1232 0,1232" fill="#1b3a6b"/>
    <polygon points="458,430 545,480 545,585 458,635 371,585 371,480" fill="#bd2a2e"/>
    <polygon points="635,535 662,551 662,583 635,599 608,583 608,551" fill="#ffffff"/>
    <polygon points="660,630 673,638 673,653 660,661 647,653 647,638" fill="#1b3a6b"/>
  </svg>
  <svg class="shapes" width="918" height="1298" viewBox="0 0 918 1298" role="img" aria-label="Photo of a desk IP phone with cloud PBX icons for applications, voicemail, fax, softphone and user portal">
    <polygon points="445,45 520,0 918,0 918,380 700,492 445,432" fill="url(#photo-tones)"/>
  </svg>

  <div class="brand abs" style="left:62px;top:62px">
    <div class="brand__square"></div>
    <div class="brand__name"><span>Gear With</span><span>Rowena</span></div>
  </div>

  <h1 class="headline abs" style="left:58px;top:212px">Plainly Talk</h1>
  <ul class="checklist abs" style="left:58px;top:300px">
    <li><svg width="22" height="22"><use href="#box-check"/></svg><span>Personalized Solutions<br>and Support</span></li>
    <li><svg width="22" height="22"><use href="#box-check"/></svg><span>Experience</span></li>
    <li><svg width="22" height="22"><use href="#box-check"/></svg><span>One Stop Shop</span></li>
  </ul>

  <div class="hex-badge abs" style="left:378px;top:478px;width:160px">We Do<br>Tech, You<br>Do You</div>

  <h2 class="seat-title abs" style="left:46px;top:582px">Seat Features</h2>
  <ul class="seat-list abs" style="left:52px;top:646px">
    <li><svg width="24" height="24"><use href="#handset"/></svg>3-Way Calling</li>
    <li><svg width="24" height="24"><use href="#handset"/></svg>Call Logs</li>
    <li><svg width="24" height="24"><use href="#handset"/></svg>Caller ID and Caller Name Delivery</li>
    <li><svg width="24" height="24"><use href="#handset"/></svg>Call Waiting</li>
    <li><svg width="24" height="24"><use href="#handset"/></svg>Call Forward Always</li>
    <li><svg width="24" height="24"><use href="#handset"/></svg>Call Forward Busy</li>
    <li><svg width="24" height="24"><use href="#handset"/></svg>Call Forward No Answer</li>
    <li><svg width="24" height="24"><use href="#handset"/></svg>Call Forward Not Reachable</li>
    <li><svg width="24" height="24"><use href="#handset"/></svg>Do Not Disturb</li>
    <li><svg width="24" height="24"><use href="#handset"/></svg>Extension Dialing</li>
    <li><svg width="24" height="24"><use href="#handset"/></svg>Last Number Redial</li>
    <li><svg width="24" height="24"><use href="#handset"/></svg>Simultaneous Ring</li>
    <li><svg width="24" height="24"><use href="#handset"/></svg>Sequential Ring</li>
    <li><svg width="24" height="24"><use href="#handset"/></svg>Speed Dial 100</li>
    <li><svg width="24" height="24"><use href="#handset"/></svg>Unified Messaging</li>
  </ul>

  <div class="pitch abs" style="left:503px;top:680px">
    <p>Do you have an older phone system that is lacking features but your worried about buying new just to get outdated again?</p>
    <p>With a cloud hosted VOIP system you can have the latest technology without expensive upfront cost. Here are just some of the many reasons and features to move to a hosted VOIP solution.</p>
  </div>
  <p class="cta abs" style="left:518px;top:1035px">Contact us today to learn how we can work with you to improve your communication tools.</p>
  <div class="contacts abs" style="left:498px;top:1130px">
    <span class="phone"><svg width="16" height="16"><use href="#phone-line"/></svg>415.639.0.517</span><br>
    <span><svg width="16" height="16" style="color:var(--red)"><use href="#mail"/></svg>sales@gearwithrowena.net</span><br>
    <span><svg width="16" height="16"><circle cx="8" cy="8" r="6" fill="none" stroke="#bd2a2e" stroke-width="1.5"/></svg>www.facebook.com/gearwithrowena</span>
  </div>

  <footer class="footer" style="padding-left:62px;font-size:24px">
    <span>Managed VOIP Phone Service</span>
    <span class="web" style="margin-left:auto;margin-right:50px;font-size:17px"><svg width="18" height="18"><use href="#globe"/></svg>www.gearwithrowena.net</span>
    <div class="footer__strip"></div>
  </footer>
</section>

<!-- BACK -->
<section class="page page--back">
  <svg class="shapes" width="918" height="1298" viewBox="0 0 918 1298">
    <polygon points="870,0 918,0 918,72 870,108 828,82 828,25" fill="#bd2a2e"/>
    <polygon points="795,38 822,54 822,85 795,101 768,85 768,54" fill="#1b3a6b"/>
    <polygon points="764,8 778,16 778,32 764,40 750,32 750,16" fill="#bd2a2e"/>
  </svg>
  <div class="brand abs" style="left:618px;top:32px;font-size:17px;gap:8px">
    <div class="brand__square" style="width:16px;height:16px"></div>
    <div class="brand__name"><span>Gear With</span><span>Rowena</span></div>
  </div>

  <h2 class="addon-title abs" style="left:52px;top:36px">Add-On Features:</h2>
  <div class="addon abs" style="left:52px;top:90px;width:380px">
    <h3>Advanced Auto Attendant</h3>
    <p>A multi-level Auto Attendant (for example, enterprise’s main Auto Attendant is configured to seamlessly route to the Auto Attendant of a particular department or location).</p>
    <h3 style="margin-top:12px">Toll-Free Numbers</h3>
    <p>An “800” number with inbound calling charged a toll to you, not the caller.</p>
  </div>
  <div class="addon abs" style="left:478px;top:90px;width:385px">
    <h3>Call Recording</h3>
    <p>Allows a user to record their calls in either an always on or ondemand mode. These recording capabilities can allow for personal monitoring or supervised monitoring of recorded calls.</p>
    <h3 style="margin-top:12px">Virtual Number</h3>
    <p>Additional phone number with unlimited incoming minutes that can be configured to point to any extension in the PBX.</p>
  </div>

  <div class="plan-head">
    <div class="plan-head__title">SERVICE PLAN</div>
    <div class="plan" style="left:374px"><div class="plan__name">Primer</div><div class="plan__sub">(Location, not a user)</div></div>
    <div class="plan" style="left:556px"><div class="plan__name">Standard</div><div class="plan__sub">(Basic user)</div></div>
    <div class="plan" style="left:729px"><div class="plan__name">Premium</div><div class="plan__sub">(Power user)</div></div>
  </div>
  <div class="price-bar">Monthly Price</div>
  <div class="price" style="left:419px">$20</div>
  <div class="price" style="left:601px">$30</div>
  <div class="price" style="left:774px">$35</div>

  <div class="plan-table">
    <div class="row"><span>Extension Dialing</span><span class="cell"><svg width="13" height="13"><use href="#tick"/></svg></span><span class="cell"><svg width="13" height="13"><use href="#tick"/></svg></span><span class="cell"><svg width="13" height="13"><use href="#tick"/></svg></span></div>
    <div class="row"><span>Local Outbound Calls Only</span><span class="cell"><svg width="13" height="13"><use href="#tick"/></svg></span><span class="cell">LD Included</span><span class="cell">LD Included</span></div>
    <div class="row"><span>Caller ID and Caller Name Delivery</span><span class="cell"><svg width="13" height="13"><use href="#tick"/></svg></span><span class="cell"><svg width="13" height="13"><use href="#tick"/></svg></span><span class="cell"><svg width="13" height="13"><use href="#tick"/></svg></span></div>
    <div class="row"><span>Call Logs</span><span class="cell"><svg width="13" height="13"><use href="#tick"/></svg></span><span class="cell"><svg width="13" height="13"><use href="#tick"/></svg></span><span class="cell"><svg width="13" height="13"><use href="#tick"/></svg></span></div>
    <div class="row"><span>Last Number Redial</span><span class="cell"><svg width="13" height="13"><use href="#tick"/></svg><small>(Local Only)</small></span><span class="cell"><svg width="13" height="13"><use href="#tick"/></svg></span><span class="cell"><svg width="13" height="13"><use href="#tick"/></svg></span></div>
    <div class="row"><span>Music On Hold</span><span class="cell"><svg width="13" height="13"><use href="#tick"/></svg></span><span class="cell"><svg width="13" height="13"><use href="#tick"/></svg></span><span class="cell"><svg width="13" height="13"><use href="#tick"/></svg></span></div>
    <div class="row"><span>Corporate Directory Access</span><span class="cell"><svg width="13" height="13"><use href="#tick"/></svg></span><span class="cell"><svg width="13" height="13"><use href="#tick"/></svg></span><span class="cell"><svg width="13" height="13"><use href="#tick"/></svg></span></div>
    <div class="row"><span>E911 Service</span><span class="cell"><svg width="13" height="13"><use href="#tick"/></svg></span><span class="cell"><svg width="13" height="13"><use href="#tick"/></svg></span><span class="cell"><svg width="13" height="13"><use href="#tick"/></svg></span></div>
    <div class="row"><span>Call Park</span><span class="cell"></span><span class="cell"><svg width="13" height="13"><use href="#tick"/></svg></span><span class="cell"><svg width="13" height="13"><use href="#tick"/></svg></span></div>
    <div class="row row--tall"><span>Call Forwarding (Always, Busy,<br>No-Answer, Not Reachable)</span><span class="cell"><svg width="13" height="13"><use href="#cross"/></svg></span><span class="cell"><svg width="13" height="13"><use href="#tick"/></svg></span><span class="cell"><svg width="13" height="13"><use href="#tick"/></svg></span></div>
    <div class="row"><span>Call Recording</span><span class="cell"><svg width="13" height="13"><use href="#cross"/></svg></span><span class="cell">Additional</span><span class="cell">Additional</span></div>
    <div class="row"><span>Call Transfer</span><span class="cell"><svg width="13" height="13"><use href="#cross"/></svg></span><span class="cell"><svg width="13" height="13"><use href="#tick"/></svg></span><span class="cell"><svg width="13" height="13"><use href="#tick"/></svg></span></div>
    <div class="row"><span>Call Waiting</span><span class="cell"><svg width="13" height="13"><use href="#cross"/></svg></span><span class="cell"><svg width="13" height="13"><use href="#tick"/></svg></span><span class="cell"><svg width="13" height="13"><use href="#tick"/></svg></span></div>
    <div class="row"><span>Unified Messaging</span><span class="cell"><svg width="13" height="13"><use href="#cross"/></svg></span><span class="cell"><svg width="13" height="13"><use href="#tick"/></svg></span><span class="cell"><svg width="13" height="13"><use href="#tick"/></svg></span></div>
    <div class="row"><span>Inclusion in Hunt Groups</span><span class="cell"><svg width="13" height="13"><use href="#cross"/></svg></span><span class="cell"><svg width="13" height="13"><use href="#tick"/></svg></span><span class="cell"><svg width="13" height="13"><use href="#tick"/></svg></span></div>
    <div class="row"><span>Simultaneous Ring</span><span class="cell"><svg width="13" height="13"><use href="#cross"/></svg></span><span class="cell"><svg width="13" height="13"><use href="#tick"/></svg></span><span class="cell"><svg width="13" height="13"><use href="#tick"/></svg></span></div>
    <div class="row"><span>Sequential Ring</span><span class="cell"><svg width="13" height="13"><use href="#cross"/></svg></span><span class="cell"><svg width="13" height="13"><use href="#tick"/></svg></span><span class="cell"><svg width="13" height="13"><use href="#tick"/></svg></span></div>
    <div class="row"><span>Speed Dial 100</span><span class="cell"><svg width="13" height="13"><use href="#cross"/></svg></span><span class="cell"><svg width="13" height="13"><use href="#tick"/></svg></span><span class="cell"><svg width="13" height="13"><use href="#tick"/></svg></span></div>
    <div class="row"><span>Three-Way Calling</span><span class="cell"><svg width="13" height="13"><use href="#cross"/></svg></span><span class="cell"><svg width="13" height="13"><use href="#tick"/></svg></span><span class="cell"><svg width="13" height="13"><use href="#tick"/></svg></span></div>
    <div class="row"><span>DeskLink Client</span><span class="cell"><svg width="13" height="13"><use href="#cross"/></svg></span><span class="cell"><svg width="13" height="13"><use href="#cross"/></svg></span><span class="cell"><svg width="13" height="13"><use href="#tick"/></svg></span></div>
    <div class="row"><span>Desktop Sharing</span><span class="cell"><svg width="13" height="13"><use href="#cross"/></svg></span><span class="cell"><svg width="13" height="13"><use href="#cross"/></svg></span><span class="cell"><svg width="13" height="13"><use href="#tick"/></svg></span></div>
    <div class="row"><span>Web Collaboration</span><span class="cell"><svg width="13" height="13"><use href="#cross"/></svg></span><span class="cell"><svg width="13" height="13"><use href="#cross"/></svg></span><span class="cell"><svg width="13" height="13"><use href="#tick"/></svg></span></div>
  </div>

  <div class="pbx-box">
    <div class="pbx-col abs" style="left:32px;top:50px;width:395px">
      <h4>Auto Attendant</h4>
      <p>An automated recording that answers the phone and provides a personalized message to callers with options for connecting to the operator, dialing by name or extension, or connecting to up to nine configurable extensions. Configuration via the Customer Portal allows for hours of operation to be modified, with different options available for hours that the company is open or closed.</p>
      <h4>Company Main Number</h4>
      <p>Phone number with unlimited incoming minutes that can be configured to point to any group extension in the PBX (such as an auto attendant or hunt group).</p>
    </div>
    <div class="pbx-col abs" style="left:458px;top:50px;width:410px">
      <h4>Corporate Directory</h4>
      <p>System Users are networked for extension to extension calling.</p>
      <h4>Hunt Groups</h4>
      <p>Allows users within a group to be included in a specified subgroup to handle incoming calls received by an assigned Hunt Group’s phone number. Within the Customer Portal, company administrators can choose from “hunt” schemes, each of which rings the specified phones in a different manner.</p>
      <h4>Music on Hold</h4>
      <p>Enables company administrators to upload an audio file (.wav file containing music, advertising, etc.) onto the system to be broadcast to parties while on hold.</p>
    </div>
  </div>
  <div class="pbx-pill">All PBX Include the Following Features:</div>

  <footer class="footer back-footer" style="padding-left:56px;height:50px">
    <span style="font-size:24px">We Do Tech, You Do You</span>
    <span class="web" style="margin-left:84px"><svg width="15" height="15"><use href="#phone-line"/></svg>415.639.0.517</span>
    <span class="web" style="margin-left:16px"><svg width="15" height="15"><use href="#mail"/></svg>sales@gearwithrowena.net</span>
    <span class="web" style="margin-left:12px"><svg width="15" height="15"><use href="#globe"/></svg>www.gearwithrowena.net</span>
    <div class="footer__strip"></div>
  </footer>
</section>
</body>
</html>
```